Lawn care business card

I am looking for a quality designed personal business card to represent the quality and elegant nature of our company. We separate ourselves in our market by the aesthetic value of our work, so I am looking for marketing material that does the same. We target our marketing high end customers, and we try to avoid price shoppers. I am open to all design options, so long as they are in line with our companies values.

We are tend to go with a retro look on everything from our logo and print material, to our uniforms. We like to portray and "old fashion" set of core values, with a modern elegance. So a wild and crazy look is out of the question.

Things I'd like on the card:
1.) Logo
2.) Phone number: (816) 555-0193
3.) Website: Verdantix.com
4.) Email: peterholloway@verdantix.com
5.) My name: Peter Holloway
6.) Facebook link: facebook.com/VerdantixGroundsandGarden
7.) Instagram: http://instagram.com/verdantix

Attached is a copy of our logo.

```html
<!DOCTYPE html>
<html lang="en">
<head>
<meta charset="utf-8">
<title>Quillmere — Peter Holloway</title>
<link rel="stylesheet" href="https://fonts.googleapis.com/css2?family=Bungee+Inline&family=Josefin+Sans:wght@400;600&display=swap">
<style>
  :root {
    --backdrop: #d9d7d2;
    --orange: #f05a1a;
    --orange-deep: #d94c12;
    --ink: #2b2b2b;
    --paper: #ffffff;
    --text: #3a3a3a;
    --social: #3b5a8a;
  }
  html, body {
    margin: 0;
    width: 1200px;
    height: 871px;
    overflow: hidden;
    background: var(--backdrop);
  }
  .card {
    position: absolute;
    left: 100px;
    top: 150px;
    width: 1000px;
    height: 572px;
    background: linear-gradient(135deg, var(--orange), var(--orange-deep));
    box-shadow: 0 10px 30px rgba(0,0,0,0.25);
  }
  .card-frame {
    position: absolute;
    inset: 0;
  }
  .brand {
    position: absolute;
    top: 88px;
    left: 0;
    right: 0;
    display: flex;
    justify-content: center;
    align-items: center;
    gap: 16px;
    font-family: "Josefin Sans", sans-serif;
    font-weight: 600;
    font-size: 56px;
    line-height: 1;
    letter-spacing: 4px;
    color: var(--orange);
  }
  .brand-dot {
    width: 26px;
    height: 26px;
    border-radius: 50%;
    background: var(--orange);
  }
  .rule {
    position: absolute;
    height: 0;
    border-top: 3px dotted var(--ink);
  }
  .rule-upper { top: 212px; left: 70px; width: 560px; }
  .rule-lower { top: 300px; left: 380px; width: 555px; }
  .holder-name {
    position: absolute;
    top: 222px;
    left: 250px;
    width: 640px;
    text-align: center;
    font-family: "Bungee Inline", sans-serif;
    font-size: 52px;
    line-height: 70px;
    color: var(--orange);
    white-space: nowrap;
  }
  .contact-row {
    position: absolute;
    top: 328px;
    left: 72px;
    right: 72px;
    display: flex;
    justify-content: space-between;
    font-family: "Josefin Sans", sans-serif;
    font-size: 21px;
    letter-spacing: 1.5px;
    text-transform: uppercase;
    color: var(--text);
    white-space: nowrap;
  }
  .social-row {
    position: absolute;
    top: 392px;
    left: 0;
    right: 0;
    display: flex;
    justify-content: center;
    gap: 48px;
    font-family: "Josefin Sans", sans-serif;
    font-size: 18px;
    letter-spacing: 1.5px;
    text-transform: uppercase;
    color: var(--text);
    white-space: nowrap;
  }
  .social-item {
    display: flex;
    align-items: center;
    gap: 10px;
  }
  .social-marker {
    width: 20px;
    height: 20px;
    border-radius: 50%;
    background: var(--social);
  }
</style>
</head>
<body>
  <div class="card">
    <svg class="card-frame" width="1000" height="572" viewBox="0 0 1000 572">
      <polygon points="80,34 920,34 920,62 966,62 966,510 920,510 920,538 80,538 80,510 34,510 34,62 80,62"
               fill="var(--ink)"/>
      <polygon points="86,40 914,40 914,68 960,68 960,504 914,504 914,532 86,532 86,504 40,504 40,68 86,68"
               fill="var(--paper)"/>
    </svg>

    <div class="brand"><span class="brand-dot"></span>QUILLMERE</div>

    <div class="rule rule-upper"></div>
    <div class="holder-name">Peter Holloway</div>
    <div class="rule rule-lower"></div>

    <div class="contact-row">
      <span class="contact-phone">(816) 555-0193</span>
      <span class="contact-email">peterholloway@quillmere.com</span>
      <span class="contact-web">Quillmere.com</span>
    </div>

    <div class="social-row">
      <span class="social-item"><span class="social-marker"></span>quillmeregroundsandgarden</span>
      <span class="social-item"><span class="social-marker"></span>@quillmere</span>
    </div>
  </div>
</body>
</html>
```